Plakat für Hersteller von maßgefertigten Tischunikaten aus Massivholz
Zielgruppe
Wir sind einen Firma die sich auf die Fertigung von maßgefertigten Tischunikaten aus Massivholz spezialisiert hat. Unsere Zielgruppe sind Design affine Leute, im Alter von 35-55 Jahren
Aufgabenstellung
Wir benötigen das Design für eine Messewand mit den Maßen 443X227 cm. 5 Zentimeter rundlaufen dürfen keine Elemente mehr platziert werden. Die Messewand steht im Hintergrund von unserem Stand bei verschiedenen Designmessen
Infos die auf die Messewand müssen: Logo, Tischmanufaktur aus Stuttgart, Maßgefertigte Tischunikate (Bei der Formulierung bin ich flexibel, ihr könnt bspw. auch nur Stichworte benutzen, aber Stuttgart und maßgefertigt ist wichtig).
Die Messewand soll sehr minimalistisch gestaltet sein, bei der letzten Messewand hatten wir ein Foto von einem Tisch im Hintergrund und das sah merkwürdig aus.

```html
<!DOCTYPE html>
<html lang="de">
<head>
<meta charset="utf-8">
<title>Holmberg Manufaktur – Messewand</title>
<link href="https://fonts.googleapis.com/css2?family=Montserrat:wght@600;700;800&display=swap" rel="stylesheet">
<style>
  :root {
    --page-bg: #e6e6e6;
    --wall-dark: #232323;
    --wall-mid: #2e2e2e;
    --wall-light: #545454;
    --text-white: #ffffff;
    --accent-green: #5a8c45;
    --accent-green-dark: #4f7f3d;
    --contour-tone: rgba(255, 255, 255, 0.05);
  }
  * { margin: 0; padding: 0; box-sizing: border-box; }
  html, body {
    width: 1200px;
    height: 816px;
    overflow: hidden;
    background: var(--page-bg);
    font-family: "Montserrat", Arial, sans-serif;
  }
  .trade-wall {
    position: absolute;
    left: 20px;
    top: 111px;
    width: 1160px;
    height: 594px;
    overflow: hidden;
    background:
      radial-gradient(ellipse 700px 520px at 0 0, var(--wall-light) 0%, var(--wall-mid) 45%, transparent 80%),
      var(--wall-dark);
    color: var(--text-white);
  }
  .contour-area {
    position: absolute;
    left: 0;
    top: 230px;
    width: 1160px;
    height: 364px;
    background: radial-gradient(ellipse 700px 260px at 75% 80%, var(--contour-tone), transparent 70%);
  }
  .brand {
    position: absolute;
    left: 61px;
    top: 40px;
    display: flex;
    align-items: center;
    gap: 11px;
  }
  .brand-circle {
    width: 76px;
    height: 76px;
    border: 4px solid var(--text-white);
    border-radius: 50%;
  }
  .brand-name {
    font-weight: 600;
    font-size: 26px;
    line-height: 31px;
  }
  .headline {
    position: absolute;
    left: 62px;
    top: 158px;
    font-weight: 800;
    font-size: 78px;
    line-height: 87px;
    letter-spacing: -1px;
    text-transform: uppercase;
  }
  .subline {
    position: absolute;
    left: 63px;
    top: 332px;
    height: 54px;
    display: flex;
    align-items: center;
    font-weight: 700;
    font-size: 38px;
    text-transform: uppercase;
  }
  .subline-city {
    margin-left: 12px;
    height: 54px;
    padding: 0 20px;
    display: flex;
    align-items: center;
    border-radius: 10px;
    background: linear-gradient(90deg, var(--accent-green), var(--accent-green-dark));
  }
  .web-address {
    position: absolute;
    right: 48px;
    top: 540px;
    font-weight: 700;
    font-size: 15px;
    letter-spacing: 0.2px;
    text-transform: uppercase;
  }
</style>
</head>
<body>
  <main class="trade-wall">
    <div class="contour-area" role="img" aria-label="Dezentes Muster aus Höhenlinien im unteren Bereich"></div>

    <div class="brand">
      <div class="brand-circle"></div>
      <div class="brand-name">Holmberg<br>Manufaktur</div>
    </div>

    <h1 class="headline">Maßgefertigte<br>Tischunikate</h1>

    <p class="subline">
      <span>Herstellung in</span>
      <span class="subline-city">Stuttgart</span>
    </p>

    <p class="web-address">www.holmberg-manufaktur.de</p>
  </main>
</body>
</html>
```